website for 'thebrightnook' which is a specialise tutoring company for children with learning difficu

We need a website for a new business that is focused on assessment and then specialised tutoring for young children with learning difficulties. The website needs to be simple but fun and fresh. We have an existing logo (uploaded) that needs to be the building block for the website. The website doesn't need to be overly content-heavy.

Target Market(s)

parents

Industry/Entity Type

Education

Number of Pages Required

3 page

Font styles to use
Other font styles liked:
• possibly matched to the logo

Requirements
Must have
• a initial front page which introduces the business and provides contact details, a second page that will allow for a more content-heavy section, a third page which focuses on introducing the staff (initially 3 staff ),

```html
<!DOCTYPE html>
<html lang="en">
<head>
<meta charset="utf-8">
<title>thebrightnook — Our Staff</title>
<link rel="stylesheet" href="https://fonts.googleapis.com/css2?family=Cinzel:wght@600;700&family=Lato:wght@400;700&family=Varela+Round&display=swap">
<style>
  :root {
    --green: #7dbb3c;
    --ink: #1d1d1d;
    --text: #3a3a3a;
    --muted: #6b6b6b;
    --panel: #f3f3f3;
    --panel-line: #cfcfcf;
    --footer-top: #dcdcdc;
    --footer-bottom: #ffffff;
    --social: #9a9a9a;
  }
  * { box-sizing: border-box; margin: 0; padding: 0; }
  html, body { width: 1117px; height: 1200px; overflow: hidden; background: #fff; }
  body { position: relative; font-family: "Lato", sans-serif; color: var(--text); }

  .hero {
    position: absolute; left: 0; top: 0; width: 1117px; height: 609px;
    background:
      radial-gradient(ellipse 260px 300px at 470px 400px, rgba(214,160,110,.55), transparent 70%),
      radial-gradient(ellipse 380px 180px at 830px 500px, rgba(190,140,90,.5), transparent 70%),
      linear-gradient(180deg, #f1f0ec 0%, #e4e0d8 45%, #b79a80 80%, #8b6a58 100%);
  }
  .hero::before {
    content: ""; position: absolute; inset: 0;
    background: linear-gradient(90deg, rgba(120,70,70,.35) 0%, transparent 25%);
  }

  .brand {
    position: absolute; left: 76px; top: 98px;
    display: flex; align-items: center; gap: 12px;
    font-family: "Lato", sans-serif; font-weight: 700; font-size: 32px;
    color: var(--ink);
  }
  .brand-mark { width: 18px; height: 18px; border-radius: 50%; background: var(--green); }

  .phone {
    position: absolute; right: 73px; top: 18px;
    display: flex; align-items: center; gap: 8px;
    font-family: "Varela Round", sans-serif; font-size: 19px; color: var(--text);
  }
  .phone-icon { width: 25px; height: 25px; }

  .main-nav { position: absolute; right: 73px; top: 68px; display: flex; gap: 35px; }
  .main-nav a {
    font-family: "Varela Round", sans-serif; font-size: 17px; color: var(--text);
    text-decoration: none; padding-bottom: 6px;
  }
  .main-nav a.is-active { color: var(--green); border-bottom: 2px solid var(--green); }

  .hero-statement {
    position: absolute; right: 73px; top: 158px; text-align: right;
    font-family: "Cinzel", serif; font-weight: 600; font-size: 24px; line-height: 34px;
    color: var(--ink);
  }

  .staff-title {
    position: absolute; left: 0; width: 1117px; top: 622px; text-align: center;
    font-family: "Cinzel", serif; font-weight: 700; font-size: 28px; color: var(--ink);
  }
  .title-divider { position: absolute; left: 424px; top: 672px; width: 268px; height: 20px; }

  .staff-photo {
    position: absolute; top: 729px; width: 174px; height: 174px; border-radius: 50%;
    border: 3px solid var(--green);
  }
  .staff-photo--one { left: 166px; background: linear-gradient(160deg, #f0ece6 0%, #d9a07a 45%, #d9532c 100%); }
  .staff-photo--two { left: 468px; background: linear-gradient(170deg, #9ea6b3 0%, #d6b28a 45%, #1f8b82 100%); }
  .staff-photo--three { left: 770px; background: linear-gradient(160deg, #e8e6e2 0%, #d8b6a0 50%, #f6f6f6 100%); }

  .staff-bio {
    position: absolute; left: 137px; top: 943px; width: 843px; height: 140px;
    background: var(--panel); border: 1px solid var(--panel-line); border-radius: 6px;
    padding: 12px 40px 0 34px;
  }
  .bio-pointer { position: absolute; left: 94px; top: -20px; width: 40px; height: 21px; }
  .bio-heading {
    display: flex; align-items: baseline; border-bottom: 1px solid var(--panel-line);
    padding-bottom: 5px;
  }
  .bio-name {
    font-family: "Varela Round", sans-serif; font-size: 23px; color: var(--green);
    border-bottom: 2px solid #555; margin-bottom: -7px; padding-bottom: 4px;
  }
  .bio-role { font-size: 16px; color: var(--muted); }
  .bio-text { margin-top: 12px; font-size: 14.6px; line-height: 21px; color: var(--text); }

  .site-footer {
    position: absolute; left: 0; top: 1115px; width: 1117px; height: 85px;
    background: linear-gradient(180deg, var(--footer-top), var(--footer-bottom));
    text-align: center;
  }
  .social-links { display: flex; justify-content: center; gap: 12px; margin-top: 22px; }
  .social-links a { width: 29px; height: 29px; border-radius: 50%; background: var(--social); display: block; }
  .copyright { margin-top: 9px; font-size: 12.5px; color: var(--ink); }
</style>
</head>
<body>
  <header class="hero" role="img" aria-label="Photo of a young girl in a yellow dress reading beside stacks of books">
  </header>

  <div class="brand"><span class="brand-mark"></span>thebrightnook</div>

  <div class="phone">
    <svg class="phone-icon" viewBox="0 0 24 24" aria-hidden="true">
      <circle cx="12" cy="12" r="12" fill="#3a3a3a"/>
      <path d="M8.2 6.5c.4-.3 1-.2 1.3.2l1.2 1.9c.2.4.1.9-.2 1.2l-.8.7c.6 1.4 1.6 2.5 3 3.1l.7-.8c.3-.4.8-.4 1.2-.2l1.9 1.2c.4.3.5.9.2 1.3l-.8 1c-.5.6-1.3.8-2 .5-3.2-1.3-5.6-3.7-6.8-6.9-.3-.7 0-1.5.5-2z" fill="var(--green)"/>
    </svg>
    555 - 014 - 2986
  </div>

  <nav class="main-nav">
    <a href="#">Home</a>
    <a href="#">Services</a>
    <a href="#" class="is-active">Our Staff</a>
  </nav>

  <p class="hero-statement">We Are A Specialized<br>Tutoring Company For<br>Children Suffering With<br>Learning Difficulties</p>

  <h1 class="staff-title">Our Staff</h1>
  <svg class="title-divider" viewBox="0 0 268 20" aria-hidden="true">
    <line x1="0" y1="10" x2="100" y2="10" stroke="var(--green)" stroke-width="1.5"/>
    <circle cx="134" cy="10" r="8" fill="#2a2a2a"/>
    <line x1="168" y1="10" x2="268" y2="10" stroke="var(--green)" stroke-width="1.5"/>
  </svg>

  <div class="staff-photo staff-photo--one" role="img" aria-label="Portrait of the science teacher"></div>
  <div class="staff-photo staff-photo--two" role="img" aria-label="Portrait of a female staff member"></div>
  <div class="staff-photo staff-photo--three" role="img" aria-label="Portrait of a male staff member in a shirt and tie"></div>

  <section class="staff-bio">
    <svg class="bio-pointer" viewBox="0 0 40 21" aria-hidden="true">
      <path d="M0 20.5 L20 0.5 L40 20.5" fill="var(--panel)" stroke="var(--panel-line)" stroke-width="1"/>
    </svg>
    <div class="bio-heading">
      <span class="bio-name">Daniel Harlow</span><span class="bio-role">, Science Teacher</span>
    </div>
    <p class="bio-text">Lorem ipsum dolor sit amet, consectetur adipiscing elit. Mauris in convallis sem. Proin cursus semper pellentesque. Pellentesque pretium est elit, vitae posuere ex vestibulum ut. Aenean tempus nulla urna, et porttitor diam varius in. Nunc blandit, ante vitae ornare blandit, nisl nibh fringilla lectus, eget porttitor dui ex at ipsum</p>
  </section>

  <footer class="site-footer">
    <div class="social-links">
      <a href="#" aria-label="Social profile one"></a>
      <a href="#" aria-label="Social profile two"></a>
      <a href="#" aria-label="Social profile three"></a>
      <a href="#" aria-label="Social profile four"></a>
    </div>
    <p class="copyright">Copyright © 2016 The Bright Nook. All Rights Reserved.</p>
  </footer>
</body>
</html>
```